distributor of aftermarket auto electrical components

I am after business card design for my new company called
Summit Vehicle Supplies (SVS as the acronym). I will supplying automotive wiring components, basically from battery to headlight. I will be aiming to sell in the 4wd scene and to auto electricians. i am not worried which colours are used though i would like it to be dynamic.
Updates

sorry guys, i have add a mobile and e-mail address that will need to on there as well. Sorry for theĀ inconvenience.

sorry guys i had erred on my spelling with my e-mail. i have now fixed it in the brief

Target Market(s)

4wd industry, custom cars, RV, auto electricians

Industry/Entity Type

Electrical

Requirements
Must have
• Company Name
ABN number: 71 306 548 290
Director: Derek Holloway
M 0432 718 946
E dhollo@fernwire.com.au

```html
<!DOCTYPE html>
<html lang="en">
<head>
<meta charset="utf-8">
<title>Summit Vehicle Supplies – Business Card</title>
<link rel="stylesheet" href="https://fonts.googleapis.com/css2?family=EB+Garamond:wght@400;500&display=swap">
<style>
  :root {
    --backdrop: #121212;
    --red-deep: #5a0a08;
    --red-mid: #9c0c0c;
    --red-bright: #d40f10;
    --silver: #a3a9a9;
    --silver-light: #e9ebeb;
    --card-light: #dfe2e2;
    --ink: #1e1e1e;
    --brand-ink: #2a2a2a;
  }
  * { margin: 0; padding: 0; box-sizing: border-box; }
  html, body {
    width: 1200px; height: 816px; overflow: hidden;
    background: var(--backdrop);
  }
  .stage { position: relative; width: 1200px; height: 816px; }
  .card {
    position: absolute; left: 360px; width: 446px; height: 219px;
    overflow: hidden;
    font-family: "EB Garamond", Georgia, serif;
    color: var(--ink);
  }
  .card--front { top: 104px; }
  .card--back { top: 412px; }
  .card__art { position: absolute; inset: 0; width: 100%; height: 100%; }
  .brand-name {
    position: absolute;
    font-family: "EB Garamond", Georgia, serif;
    font-weight: 500;
    color: var(--brand-ink);
    letter-spacing: 1.5px;
    text-transform: uppercase;
    white-space: nowrap;
  }
  .card--front .brand-name {
    left: 0; right: 0; top: 96px; text-align: center; font-size: 25px;
  }
  .card--back .brand-name {
    right: 14px; top: 56px; text-align: right; font-size: 15px; letter-spacing: 1.2px;
  }
  .contact { position: absolute; left: 288px; top: 128px; width: 152px; }
  .contact__name { font-size: 22px; line-height: 1; font-weight: 400; white-space: nowrap; }
  .contact__role { font-size: 12px; line-height: 1.2; margin-top: 2px; }
  .contact__details { list-style: none; font-size: 10.5px; line-height: 1.08; margin-top: 3px; padding-left: 2px; white-space: nowrap; }
</style>
</head>
<body>
<main class="stage">
  <section class="card card--front" aria-label="Card front">
    <svg class="card__art" viewBox="0 0 446 219" aria-hidden="true">
      <defs>
        <linearGradient id="frontRed" x1="0" y1="0" x2="0" y2="1">
          <stop offset="0" stop-color="#6e0606"/>
          <stop offset="1" stop-color="#c20d0d"/>
        </linearGradient>
        <radialGradient id="frontSilver" cx="0.5" cy="0.6" r="0.6">
          <stop offset="0" stop-color="var(--silver-light)"/>
          <stop offset="1" stop-color="var(--silver)"/>
        </radialGradient>
      </defs>
      <rect width="446" height="219" fill="url(#frontRed)"/>
      <path d="M0 88 Q40 96 60 92 L386 92 Q410 96 446 88 L446 219 L0 219 Z" fill="url(#frontSilver)"/>
    </svg>
    <p class="brand-name">Summit Vehicle Supplies</p>
  </section>

  <section class="card card--back" aria-label="Card back">
    <svg class="card__art" viewBox="0 0 446 219" aria-hidden="true">
      <defs>
        <linearGradient id="backRed" x1="0" y1="0" x2="1" y2="0">
          <stop offset="0" stop-color="var(--red-deep)"/>
          <stop offset="0.5" stop-color="var(--red-mid)"/>
          <stop offset="0.65" stop-color="var(--red-bright)"/>
        </linearGradient>
      </defs>
      <rect width="446" height="219" fill="url(#backRed)"/>
      <path d="M258 0 C200 8 178 40 186 90 C192 140 262 170 285 219 L446 219 L446 0 Z" fill="var(--card-light)"/>
    </svg>
    <p class="brand-name">Summit Vehicle Supplies</p>
    <div class="contact">
      <h1 class="contact__name">Derek Holloway</h1>
      <p class="contact__role">Director</p>
      <ul class="contact__details">
        <li>abn: 71 306 548 290</li>
        <li>m: 0432 718 946</li>
        <li>e-mail: dhollo@fernwire.com.au</li>
      </ul>
    </div>
  </section>
</main>
</body>
</html>
```